Visitenkarte erstellen für Reiki Praxis

Visitenkarten für Reiki Praxis Doppelseitig

business cards reiki practice double-sided

The background can also be a different color

```html
<!DOCTYPE html>
<html lang="en">
<head>
<meta charset="utf-8">
<title>Lumen Reiki – Business Card</title>
<link rel="stylesheet" href="https://fonts.googleapis.com/css2?family=Open+Sans:wght@400&family=Montserrat:wght@400;500&display=swap">
<style>
  :root {
    --page-bg: #d4d5d7;
    --card-bg: #2f1a35;
    --card-bg-light: #351d3b;
    --gold: #e8b424;
    --white: #ffffff;
    --mark-line: #d9b98a;
  }
  * { margin: 0; padding: 0; box-sizing: border-box; }
  html, body {
    width: 900px; height: 1200px; overflow: hidden;
    background: var(--page-bg);
  }
  .card {
    position: absolute;
    left: 170px;
    width: 563px; height: 363px;
    border-radius: 30px;
    background: linear-gradient(160deg, var(--card-bg-light), var(--card-bg));
    color: var(--white);
  }
  .card--front { top: 196px; }
  .card--back { top: 630px; }

  /* Front */
  .brand-mark {
    position: absolute; left: 50%; top: 118px;
    width: 60px; height: 60px; margin-left: -30px;
    border: 1.5px solid var(--mark-line); border-radius: 50%;
  }
  .brand-name {
    position: absolute; left: 0; right: 0; top: 198px;
    text-align: center;
    font-family: "Open Sans", sans-serif; font-weight: 400;
    font-size: 31px; letter-spacing: 0.2px; color: var(--white);
  }
  .owner-name {
    position: absolute; left: 0; right: 0; top: 236px;
    text-align: center;
    font-family: "Montserrat", sans-serif; font-weight: 400;
    font-size: 22px; letter-spacing: 6px; color: var(--gold);
  }

  /* Back */
  .identity {
    position: absolute; right: 302px; top: 155px; text-align: right;
    font-family: "Montserrat", sans-serif;
  }
  .identity__name {
    font-size: 24px; font-weight: 400; color: var(--gold); letter-spacing: 0.5px; line-height: 30px;
  }
  .identity__role { font-size: 13px; color: var(--white); letter-spacing: 0.6px; margin-top: 2px; }
  .divider {
    position: absolute; left: 281px; top: 146px;
    width: 1.5px; height: 70px; background: var(--white);
  }
  .contacts {
    position: absolute; left: 300px; top: 147px; list-style: none;
    font-family: "Montserrat", sans-serif; font-size: 13.5px; letter-spacing: 0.6px;
  }
  .contacts li { display: flex; align-items: center; height: 23.5px; }
  .contacts svg { width: 11px; height: 11px; margin-right: 8px; fill: var(--gold); }
  .social {
    position: absolute; left: 0; right: 0; top: 307px;
    display: flex; justify-content: center; align-items: center; gap: 6px;
    font-family: "Montserrat", sans-serif; font-size: 13px; letter-spacing: 0.6px;
    padding-left: 2px;
  }
  .social__label { margin-right: 2px; }
  .social__dot { width: 23px; height: 23px; border: 2px solid var(--gold); border-radius: 50%; }
</style>
</head>
<body>
  <section class="card card--front">
    <div class="brand-mark"></div>
    <div class="brand-name">LUMEN REIKI</div>
    <div class="owner-name">MARA VENN</div>
  </section>

  <section class="card card--back">
    <div class="identity">
      <div class="identity__name">MARA VENN</div>
      <div class="identity__role">Founder</div>
    </div>
    <div class="divider"></div>
    <ul class="contacts">
      <li>
        <svg viewBox="0 0 24 24" aria-hidden="true"><path d="M6.6 10.8a15.1 15.1 0 0 0 6.6 6.6l2.2-2.2c.3-.3.7-.4 1-.2 1.1.4 2.3.6 3.6.6.6 0 1 .4 1 1V20c0 .6-.4 1-1 1A17 17 0 0 1 3 4c0-.6.4-1 1-1h3.5c.6 0 1 .4 1 1 0 1.3.2 2.5.6 3.6.1.3 0 .7-.2 1l-2.3 2.2z"/></svg>
        07911482650
      </li>
      <li>
        <svg viewBox="0 0 24 24" aria-hidden="true"><path d="M2 5h20v14H2z M2 5l10 8 10-8" fill="none" stroke="#e8b424" stroke-width="0"/><path d="M2 5h20L12 12.5z M2 7l7 5.5L2 18z M22 7v11l-7-5.5z M10.5 13.6 12 14.8l1.5-1.2L21 19H3z"/></svg>
        mara.venn@lumenreiki.com
      </li>
      <li>
        <svg viewBox="0 0 24 24" aria-hidden="true"><path d="M12 2a10 10 0 1 0 0 20 10 10 0 0 0 0-20zm0 2c.9 1.2 1.6 2.6 2 4h-4c.4-1.4 1.1-2.8 2-4zM4.3 14a8 8 0 0 1 0-4h3.4a16 16 0 0 0 0 4H4.3zm.8 2h3c.3 1.3.8 2.5 1.4 3.6A8 8 0 0 1 5.1 16zm3-8h-3a8 8 0 0 1 4.4-3.6C8.9 5.5 8.4 6.7 8.1 8zM12 20c-.9-1.2-1.6-2.6-2-4h4c-.4 1.4-1.1 2.8-2 4zm2.3-6H9.7a14 14 0 0 1 0-4h4.6a14 14 0 0 1 0 4zm.2 5.6c.6-1.1 1.1-2.3 1.4-3.6h3a8 8 0 0 1-4.4 3.6zm1.8-5.6a16 16 0 0 0 0-4h3.4a8 8 0 0 1 0 4h-3.4zm-.4-6c-.3-1.3-.8-2.5-1.4-3.6A8 8 0 0 1 18.9 8h-3z"/></svg>
        www.lumenreiki.com
      </li>
    </ul>
    <div class="social">
      <span class="social__label">follow us on:</span>
      <span class="social__dot"></span>
      <span class="social__dot"></span>
    </div>
  </section>
</body>
</html>
```